Meridale Sonography Academy (Meridale Institute of Scan Studies) needs an additional web design f

Don't require a redesign of our existing website, I need an additional web design to compliment and feed into our existing web page (kplv.edu.au) but establish excellent google rankings in it's own right. Web page is to appeal to a specific target market in the allied health industry who wish to learn how to do ultrasound on patients. New website is www. rapidsonarskillsnet.com.au. Our educational institution delivers hands on workshops and seminars on ANYTHING involved with EMERGENCY Ultrasound - intro, advanced, doctors, nurses, etc. Our competitors in this field www.scanlearnhub.com.au and www.bqo.edu.au. Looking for a design that will capture the target audience and deliver the message that the courses are delivered by one of the best faculties in Australia. SEO strategies are paramount in that we don't wish to be penalised by Google by running a feeder site. Courses are delivered in Sydney and are accredited by an organisation called TVRE.com.au. The courses are listed under 2 qualifications on TVRE website - PLDX and RWMTZ. Registrants of our courses are striving to achieve either PLDX - Diploma in Bedside Operator Scan Skills http://www.tvre.com.au/newsite/Files/Documents/Education/PLDX/PLDX_Course_Brochure.pdf OR RWMTZ - Diploma in Support Staff Operated Scan Skills http://www.tvre.com.au/newsite/Files/Documents/Education/RWMTZ/RWMTZ_Course_Brochure.pdf.
Website to be iphone, smartphone and tablet compatible.

Target Market(s)

Emergency Physicians and Emergency nurses/doctors.

Industry/Entity Type

School

Coding

Coded - Design and coding required

Number of Pages Required

2 page

Font styles to use
Other font styles liked:
• See website http://www.brightfolddental.com.au/

Colors
86cae6
ec1f27

Requirements
Must have
• Overall professional feel but easy to read and informative.
• Links to our normal website pages www.kplv.edu.au
• Ability to rank high.
• Copy of material we deliver here http://www.kplv.edu.au/acute-scan-class-1-3-days/ Click through on relevant dates for more information.
Nice to have
• I like this website - font, feel, layout etc.
• http://www.brightfolddental.com.au/
Should not have
• Information that will lower our google rankings knowing it is linked to www.kplv.edu.au

```html
<!DOCTYPE html>
<html lang="en">
<head>
<meta charset="utf-8">
<title>Meridale Sonography Academy – Emergency Ultrasound Training</title>
<link href="https://fonts.googleapis.com/css2?family=Open+Sans:wght@300;400;600;700&display=swap" rel="stylesheet">
<style>
:root{
  --red:#e0242b;
  --sky:#86cae6;
  --link:#2d63b0;
  --ink:#333;
  --muted:#666;
  --line:#dcdcdc;
  --nav:#2b2b2b;
  --band:#2c3539;
  --footer:#2a2a2a;
  --base:#1f1f1f;
  --teal:#4fb7a0;
  --white:#fff;
}
*{box-sizing:border-box;margin:0;padding:0}
html,body{width:741px;height:1200px;overflow:hidden}
body{position:relative;background:var(--white);font-family:"Open Sans",Arial,sans-serif;color:var(--ink);font-size:6px;line-height:1.5}
.abs{position:absolute}
ul{list-style:none}

/* header */
.site-name{left:149px;top:17px;font-size:14px;font-weight:400;color:#111;letter-spacing:.2px}
.search{left:451px;top:15px;width:74px;height:10px;border:1px solid #ccc;font-size:5px;color:#999;padding:1px 3px;line-height:7px}
.social{left:526px;top:15px;display:flex;gap:1px}
.social span{width:9px;height:10px;display:block}
.contact-top{left:470px;top:30px;width:123px;text-align:right;font-size:5px;color:#888}

/* navigation */
.main-nav{left:0;top:53px;width:741px;height:23px;background:var(--nav)}
.main-nav ul{position:absolute;left:150px;top:0;display:flex;height:23px}
.main-nav li{color:var(--white);font-size:5.6px;padding:0 8px;line-height:23px;border-right:1px solid #3c3c3c;display:flex;align-items:center;gap:3px}
.main-nav li:first-child{border-left:1px solid #3c3c3c}
.main-nav li.active{background:#383838}
.main-nav svg{width:5px;height:5px}

/* hero */
.hero{left:0;top:76px;width:741px;height:225px;background:radial-gradient(ellipse at 30% 30%,#e0306a 0%,#a0163e 35%,#5a0c2a 70%,#2a0616 100%)}
.hero-arrow{top:181px;width:14px;height:14px}

/* welcome */
.welcome-title{left:0;top:330px;width:741px;text-align:center;font-size:11px;font-weight:400;color:#444}
.welcome-title b{font-weight:700;color:#222}
.welcome-intro{left:149px;top:346px;width:444px;text-align:center;font-size:5.5px;color:var(--muted)}
.feature{top:380px;width:140px;text-align:center}
.feature .icon{width:22px;height:22px;margin:0 auto 4px}
.feature h3{font-size:7px;font-weight:400;color:#555;margin-bottom:2px}
.feature p{font-size:5.3px;color:var(--muted);line-height:1.55;height:30px}
.btn-red{display:inline-block;background:var(--red);color:var(--white);font-size:4.5px;padding:1px 6px;border-radius:1px;line-height:7px}
.divider-v{top:378px;width:1px;height:84px;background:var(--line)}

/* events */
.events{left:0;top:491px;width:741px;height:157px;background:var(--band)}
.events .machine{left:147px;top:6px;width:158px;height:141px;background:radial-gradient(ellipse at 50% 55%,#8a95a0 0%,#56616b 45%,#2c3539 75%)}
.events .pen{left:454px;top:22px;width:16px;height:16px}
.events h2{left:311px;top:48px;width:290px;text-align:center;font-size:9px;font-weight:400;color:var(--white)}
.events h2 b{font-weight:700}
.events .event-name{left:311px;top:62px;width:290px;text-align:center;font-size:7.5px;color:var(--sky)}
.events .event-date{left:311px;top:78px;width:290px;text-align:center;font-size:5px;color:#ddd}
.events .event-desc{left:311px;top:92px;width:282px;font-size:5.6px;color:#e8e8e8;line-height:1.75}
.events .more{left:527px;top:132px;font-size:5.6px;color:var(--white);display:flex;align-items:center;gap:4px}

/* about tabs */
.tabs{left:149px;top:681px;width:211px;height:97px;border:1px solid var(--line);border-radius:3px}
.tabs .tab-row{display:flex;border-bottom:1px solid var(--line);height:14px}
.tabs .tab{font-size:5.3px;padding:0 8px;line-height:14px;color:#555;border-right:1px solid var(--line);display:flex;align-items:center;gap:3px}
.tabs .tab.active{color:var(--red);border-bottom:1px solid var(--white);margin-bottom:-1px;background:var(--white)}
.tabs .tab svg{width:5px;height:5px}
.tabs p{font-size:5.3px;color:#444;padding:5px 8px 0;line-height:1.6}
.tabs .more{position:absolute;right:8px;bottom:3px;font-size:5.3px;color:var(--red);display:flex;align-items:center;gap:3px}

.info-title{left:381px;top:680px;font-size:6.5px;color:#555}
.skill{left:381px;width:211px}
.skill .label{font-size:5.3px;color:#444}
.skill .track{height:4px;background:#eee;border-radius:2px;position:relative}
.skill .fill{height:4px;background:var(--red);border-radius:2px}
.skill .pct{position:absolute;top:-7px;font-size:4px;color:#444}

/* course columns */
.col-title{font-size:6.5px;color:var(--red);font-weight:400}
.course-a{left:149px;top:808px;width:140px}
.course-a .org{font-size:4.8px;color:#444;margin-top:6px;line-height:1.45}
.course-a h4{font-size:4.8px;font-weight:400;margin-top:3px}
.circle-list li{font-size:4.8px;color:#444;display:flex;align-items:center;gap:4px;margin-top:3.6px;padding-left:2px}
.circle-list li::before{content:"";width:4px;height:4px;border:0.7px solid #777;border-radius:50%;flex:none}
.course-a .faculty{font-size:4.8px;color:#444;margin-top:4px;line-height:2.3}

.course-b{left:303px;top:808px;width:140px}
.topic-box{margin-top:8px;width:135px;border:1px solid var(--line);padding:4px 8px 6px}
.topic-box li{font-size:4.8px;color:#444;display:flex;align-items:center;gap:5px;line-height:13.6px}
.topic-box li::before{content:"";width:6px;height:6px;border-radius:50%;background:var(--red);flex:none}
.course-b .limited{font-size:6px;font-weight:600;color:#444;margin-top:8px;line-height:1.35}
.course-b p{font-size:5.2px;color:#444;margin-top:4px;line-height:1.55}

.course-c{left:457px;top:808px;width:136px}
.date-box{margin-top:8px;width:136px;height:156px;border:1px solid var(--line);border-radius:2px;padding:5px 8px}
.date-box li{font-size:4.6px;color:var(--link);line-height:1.4;margin-bottom:7.3px}
.date-box .addon{font-size:4.6px;color:#444;font-weight:600;margin:3px 0 8px;line-height:1.45}
.date-box .addon span{font-weight:400}

/* call to action */
.cta{left:0;top:1036px;width:741px;height:33px;background:var(--footer)}
.cta p{position:absolute;left:149px;top:9px;font-size:9px;color:var(--white)}
.cta .register{position:absolute;left:467px;top:9px;width:125px;height:15px;background:var(--white);color:#222;font-size:9px;text-align:center;line-height:15px}
.stripe{left:0;top:1069px;width:741px;height:3px;display:flex}
.stripe span{flex:1}

/* footer */
.site-footer{left:0;top:1072px;width:741px;height:112px;background:var(--footer)}
.f-col{top:24px;width:150px}
.f-col h5{font-size:6.5px;font-weight:400;color:#9a9a9a;margin-bottom:5px}
.f-col li{font-size:5.5px;color:#cfcfcf;line-height:11.7px}
.f-col .note{font-size:5.5px;color:#cfcfcf;line-height:11.7px}
.f-col .sub{font-size:6.5px;color:#9a9a9a;margin-top:1px}
.base-bar{left:0;top:1184px;width:741px;height:16px;background:var(--base)}
.base-bar .copy{position:absolute;left:149px;top:4px;font-size:5px;color:#999}
.base-bar ul{position:absolute;right:146px;top:4px;display:flex;gap:28px;font-size:5px;color:#999}
</style>
</head>
<body>

<header>
  <div class="abs site-name">Meridale Sonography Academy</div>
  <div class="abs search">Search...</div>
  <div class="abs social" aria-label="Search and social links">
    <span style="background:#555"></span>
    <span style="background:#3aa3dd"></span>
    <span style="background:#3b5c9a"></span>
    <span style="background:#e0467c"></span>
    <span style="background:#1f78b4"></span>
    <span style="background:#f29a1d"></span>
  </div>
  <div class="abs contact-top">&#9742; 1234567890 &nbsp;&nbsp; &#9993; info@meridalesono.com</div>
</header>

<nav class="abs main-nav">
  <ul>
    <li class="active"><svg viewBox="0 0 10 10"><path d="M1 5 5 1 9 5V9H1Z" fill="#fff"/></svg>Home</li>
    <li><svg viewBox="0 0 10 10"><circle cx="5" cy="5" r="4" fill="#fff"/></svg>About us</li>
    <li><svg viewBox="0 0 10 10"><path d="M2 2H8V8H2Z" fill="#fff"/></svg>Seminars</li>
    <li><svg viewBox="0 0 10 10"><path d="M2 8 8 2" stroke="#fff" stroke-width="2"/></svg>Become a sonographer</li>
    <li><svg viewBox="0 0 10 10"><path d="M1 2H9V7H1ZM3 9H7" stroke="#fff" fill="none" stroke-width="1.4"/></svg>Consulting</li>
    <li><svg viewBox="0 0 10 10"><rect x="2" y="2" width="6" height="6" fill="none" stroke="#fff" stroke-width="1.4"/></svg>Models</li>
    <li><svg viewBox="0 0 10 10"><path d="M2 5A3 3 0 1 1 5 8" stroke="#fff" fill="none" stroke-width="1.4"/></svg>Information</li>
    <li><svg viewBox="0 0 10 10"><path d="M1 2H9V8H1ZM1 2 5 5 9 2" stroke="#fff" fill="none" stroke-width="1.2"/></svg>Contact us</li>
  </ul>
</nav>

<section class="abs hero" role="img" aria-label="Photo of a cheerful group of students holding a sign reading Ultrasound Training Specialists, against a red and magenta lit background"></section>
<svg class="abs hero-arrow" style="left:9px" viewBox="0 0 14 14"><circle cx="7" cy="7" r="6.3" fill="#111" stroke="#fff" stroke-width="1"/><path d="M8 4 5 7 8 10" stroke="#fff" fill="none" stroke-width="1.3"/></svg>
<svg class="abs hero-arrow" style="left:717px" viewBox="0 0 14 14"><circle cx="7" cy="7" r="6.3" fill="#111" stroke="#fff" stroke-width="1"/><path d="M6 4 9 7 6 10" stroke="#fff" fill="none" stroke-width="1.3"/></svg>

<section class="welcome">
  <h1 class="abs welcome-title">Welcome to our <b>world</b> Excellence in <b>practical</b> education!</h1>
  <p class="abs welcome-intro">Commune mentitum tincidunt ei eos, ut nostro deleniti sea, has nam omnesque delicata et. Pri te eius imperdiet evertitur. Eu ipsum soleat platonem pri, brute honestatis cu eam, nonumes aliquid accommodare te nam. Nobis complectitur in duo</p>

  <div class="abs feature" style="left:146px">
    <svg class="icon" viewBox="0 0 22 22"><circle cx="11" cy="11" r="10" fill="none" stroke="#e0242b" stroke-width="1.2"/><circle cx="11" cy="9" r="2.4" fill="#e0242b"/><path d="M6.5 16a4.5 4 0 0 1 9 0Z" fill="#e0242b"/></svg>
    <h3>Patient Models</h3>
    <p>There is a severe shortage of people trained in Medical Ultrasound (Sonography) throughout Australia including Sydney</p>
    <span class="btn-red">Read more</span>
  </div>
  <div class="abs divider-v" style="left:296px"></div>
  <div class="abs feature" style="left:300px">
    <svg class="icon" viewBox="0 0 22 22"><circle cx="11" cy="11" r="10" fill="none" stroke="#e0242b" stroke-width="1.2"/><path d="M6 8h10v6H10l-3 2v-2H6Z" fill="#e0242b"/></svg>
    <h3>Pregnant Models</h3>
    <p>Obstetric (pregnancy) models in their 1st, 2nd and 3rd Trimesters find it very exciting to come in and have a look at their babies in</p>
    <span class="btn-red">Read more</span>
  </div>
  <div class="abs divider-v" style="left:446px"></div>
  <div class="abs feature" style="left:453px">
    <svg class="icon" viewBox="0 0 22 22"><circle cx="11" cy="11" r="10" fill="none" stroke="#e0242b" stroke-width="1.2"/><rect x="6" y="7" width="10" height="8" fill="none" stroke="#e0242b" stroke-width="1.2"/><path d="M7 14 10 10.5 12 12.5 13.5 11 15 14Z" fill="#e0242b"/></svg>
    <h3>Previous Models' Experiences</h3>
    <p>MISS is seeking past models for its regular training sessions held throughout the year at its campus in Pellam St, Ashcombe</p>
    <span class="btn-red">Read more</span>
  </div>
</section>

<section class="abs events">
  <div class="abs machine" role="img" aria-label="Product photo of an ultrasound scanning machine beside a patient examination couch"></div>
  <svg class="abs pen" viewBox="0 0 16 16"><path d="M3 13 4 9 11 2 14 5 7 12Z" fill="none" stroke="#86cae6" stroke-width="1.3"/><path d="M3 13 6 12" stroke="#86cae6" stroke-width="1.3"/></svg>
  <h2 class="abs">New / Upcoming <b>Events</b> and Seminars</h2>
  <div class="abs event-name">5day Obstetrics scanning workshop (October)</div>
  <div class="abs event-date">October 22, 2014 9:00 am - October 26, 2014 4:30 pm</div>
  <p class="abs event-desc">Course description: Accreditation: TVRE CPD This 5 day "hands on" introductory course is designed for trainee Sonographers beginning of their ultrasound training in obstetric ultrasound. Curriculum: Physical principles and artifacts ...</p>
  <div class="abs more">Read more <svg width="10" height="5" viewBox="0 0 10 5"><path d="M0 2.5H9M7 .5 9 2.5 7 4.5" stroke="#fff" fill="none" stroke-width=".8"/></svg></div>
</section>

<section class="abs tabs">
  <div class="tab-row">
    <span class="tab active"><svg viewBox="0 0 10 10"><ellipse cx="5" cy="5" rx="4.3" ry="2.6" fill="none" stroke="#e0242b"/><circle cx="5" cy="5" r="1.3" fill="#e0242b"/></svg>Our Vision</span>
    <span class="tab"><svg viewBox="0 0 10 10"><path d="M2 8 8 2M5 2H8V5" stroke="#555" fill="none" stroke-width="1.2"/></svg>Our Mission</span>
    <span class="tab"><svg viewBox="0 0 10 10"><circle cx="5" cy="5" r="4" fill="none" stroke="#555"/><path d="M5 2.5V5H7" stroke="#555" fill="none"/></svg>Our History</span>
  </div>
  <p>MISS develops and produces the highest quality graduates, recruitment solutions and training programs for the medical imaging and allied health workforce in both Australia and overseas.Our vision is to maintain and cement our position as leaders of quality ultrasound education through continuous improvement and development of the faculty, quality and range of seminars with the highest levels of customer service and satisfaction</p>
  <div class="more">Read More <svg width="8" height="5" viewBox="0 0 8 5"><path d="M0 2.5H7M5 .5 7 2.5 5 4.5" stroke="#e0242b" fill="none" stroke-width=".8"/></svg></div>
</section>

<section class="skills">
  <h3 class="abs info-title" style="font-weight:400">MISS INFORMATION</h3>
  <div class="abs skill" style="top:697px"><div class="label">Seminars and Ultrasound Training on Demand</div><div class="track"><div class="fill" style="width:80%"></div><span class="pct" style="left:76%">80%</span></div></div>
  <div class="abs skill" style="top:717px"><div class="label">Become a Sonographer</div><div class="track"><div class="fill" style="width:90%"></div><span class="pct" style="left:86%">90%</span></div></div>
  <div class="abs skill" style="top:736px"><div class="label">Register to be an MISS Model</div><div class="track"><div class="fill" style="width:60%"></div><span class="pct" style="left:56%">60%</span></div></div>
  <div class="abs skill" style="top:755px"><div class="label">Venue information</div><div class="track"><div class="fill" style="width:70%"></div><span class="pct" style="left:66%">70%</span></div></div>
</section>

<section class="abs course-a">
  <h3 class="col-title">Emergency Ultrasound Course</h3>
  <div class="org">MERIDALE INSTITUTE OF SCAN STUDIES<br>AND SONAR COMMONS</div>
  <h4>FEATURES:</h4>
  <ul class="circle-list">
    <li>Online Lectures – Prerequisite physics</li>
    <li>Maximal hands on scanning time</li>
    <li>Structured Reports</li>
    <li>Opportunity for Logbook submission</li>
  </ul>
  <h4>DESIGNED AND DELIVERED BY:</h4>
  <ul class="circle-list">
    <li>Emergency Physicians (with post graduate Ultrasound qualifications</li>
    <li>Sonographers</li>
    <li>Medical Educationalists</li>
  </ul>
  <div class="faculty">Dr Lena Harwick (Eastvale Hospital<br>Dr Tomas Beland (Northgate General Hospital<br>Prof Rhea Calder (Riverbend District Hospital</div>
</section>

<section class="abs course-b">
  <h3 class="col-title">EMERGENCY ULTRASOUND COURSE – 2 DAYS</h3>
  <ul class="topic-box">
    <li>(ABDOMINAL AORTIC ANEURYSM (AAA)</li>
    <li>ULTRASOUND ESSENTIALS</li>
    <li>E-FAST</li>
    <li>VASCULAR ACCESS</li>
    <li>FOREIGN BODIES</li>
    <li>DVT</li>
  </ul>
  <div class="limited">LIMITED NUMBERS WILL APPLY TO MAXIMIZE HANDS ON LEARNING</div>
  <p>This course has been accredited by CMEB and TVRE for AAA, E-FAST, Vascular Access, DVT and Basic Cardi-ac. Please see Sonar Commons for accreditation details<br>Approved for RURAL GP GRANTS FOR EMERGENCY</p>
</section>

<section class="abs course-c">
  <h3 class="col-title">Book this seminar</h3>
  <div class="date-box">
    <ul>
      <li>from 8:00 AM to 30/01/2015 3:00 PM 29/01/2015</li>
      <li>from 8:00 AM to 15/05/2015 3:00 PM 14/05/2015</li>
      <li>from 8:00 AM to 04/09/2015 3:00 PM 03/09/2015</li>
    </ul>
    <div class="addon">EMERGENCY ULTRASOUND COURSE<br>DAY Add on option 1 -<br><span>(BASIC ECHOCARDIOGRAPHY IN LIFE SUPPORT (BELS)</span></div>
    <ul>
      <li>from 8:00 AM to 31/01/2015 3:00 PM 31/01/2015</li>
      <li>from 8:00 AM to 16/05/2015 3:00 PM 16/05/2015</li>
      <li>from 8:00 AM to 05/09/2015 3:00 PM 05/09/2015</li>
    </ul>
  </div>
</section>

<section class="abs cta">
  <p>Interested? Find a Seminar or Course and register with Ultrasound</p>
  <span class="register">REGISTER ONLINE</span>
</section>
<div class="abs stripe"><span style="background:var(--red)"></span><span style="background:var(--teal)"></span><span style="background:var(--sky)"></span></div>

<footer class="abs site-footer">
  <div class="abs f-col" style="left:149px">
    <h5>SONOGRAPHY</h5>
    <ul><li>GPMU Program Overview</li><li>ISP Program Overview</li><li>ISIP Trainee Testimonials</li><li>Meet some past students</li></ul>
  </div>
  <div class="abs f-col" style="left:303px">
    <h5>INFORMATION</h5>
    <ul><li>Accommodation</li><li>Local Information</li><li>Useful Links</li><li>Venue Information</li></ul>
  </div>
  <div class="abs f-col" style="left:457px">
    <h5>CONTACT INFORMATION</h5>
    <div class="note">Ut pri noster corpora an erpuit feugiat id vel<br>novum libris inermis<br>Contact Us</div>
    <div class="sub">STUDENT ONLINE RESOURCE</div>
  </div>
</footer>
<div class="abs base-bar">
  <span class="copy">Copyright 2014, Tri-Forge. All rights reserved.</span>
  <ul><li>Home</li><li>About us</li><li>Seminars</li></ul>
</div>

</body>
</html>
```